SKYVANTEX (drone photo and video) and Photogrammetry Services (mapping and 3D modeling)

We need a business card design for a SKYVANTEX. Our businesses provides (drone) Aerial Photo and Video Captures. However we also provide Photogrammetry (which is 3D modeling and mapping). We greatly value unique points of view taken of landscapes and subjects with aerial photography and videography. 3D modeling and mapping is the other area of focus and have an incredibly broad scope of applications and imaginative creativity.

Target Market(s)

Based out of Northern Virginia and serving the greater Virginia and Maryland areas

Industry/Entity Type

Drone Photo and video and Photogrammetry Services (mapping and 3D modeling)

Contact Information for Business Card

3D Models, Maps and Photo/Video Production name: Marcus Pettibone email: mqp@skyvantex.us website: skyvantex.us phone: 571-806-3394; please also include "Aerial Photo/Video and 3D Mapping/Modeling"

Requirements
Must have
• Please make this design vertical and double sided. The selection box is not letting me choose Double Sided but that is my wish. Incorporate uploaded LOGO and color scheme
Nice to have
• Preferably does not feel too crowded and balances not having an exaggerated amount of distracting detail
Should not have
• do not cram bullet points or text in long form

```html
<!DOCTYPE html>
<html lang="en">
<head>
<meta charset="utf-8">
<title>SKYVANTEX Business Card</title>
<link href="https://fonts.googleapis.com/css2?family=Roboto+Condensed:wght@400;700&display=swap" rel="stylesheet">
<style>
  :root {
    --backdrop: #e4e4e2;
    --card-light: #ffffff;
    --card-dark: #222b34;
    --accent-red: #e3201b;
    --ink: #1a1a1a;
    --muted: #5b6168;
    --slate: #6f8593;
    --slate-light: #8fa3af;
    --photo-dark: #3c3f44;
    --photo-mid: #74777c;
    --photo-light: #eef0f2;
    --shadow: rgba(0, 0, 0, 0.22);
  }
  * { margin: 0; padding: 0; box-sizing: border-box; }
  html, body {
    width: 1200px;
    height: 846px;
    overflow: hidden;
    background: var(--backdrop);
    font-family: "Roboto Condensed", "Arial Narrow", sans-serif;
  }
  .canvas {
    position: relative;
    width: 1200px;
    height: 846px;
  }
  .card {
    position: absolute;
    box-shadow: 10px 12px 14px var(--shadow);
  }
  .card--front {
    left: 172px;
    top: 169px;
    width: 290px;
    height: 508px;
    background: var(--card-light);
  }
  .card--back {
    left: 519px;
    top: 278px;
    width: 508px;
    height: 290px;
    background: var(--card-dark);
  }
  .brand {
    position: absolute;
    left: 0;
    width: 100%;
    display: flex;
    align-items: center;
    justify-content: center;
    font-weight: 700;
  }
  .card--front .brand {
    top: 62px;
    gap: 10px;
    font-size: 32px;
    letter-spacing: 1px;
    color: var(--accent-red);
  }
  .card--front .brand__dot {
    width: 22px;
    height: 22px;
    border-radius: 50%;
    background: var(--accent-red);
  }
  .identity {
    position: absolute;
    left: 0;
    top: 116px;
    width: 100%;
    text-align: center;
  }
  .identity__name {
    font-size: 18px;
    font-weight: 700;
    color: var(--ink);
  }
  .identity__tagline {
    margin-top: 3px;
    font-size: 12.5px;
    color: var(--muted);
  }
  .contact-list {
    position: absolute;
    left: 53px;
    top: 178px;
    list-style: none;
  }
  .contact-list li {
    display: flex;
    align-items: center;
    height: 31px;
    font-size: 19px;
    color: var(--ink);
  }
  .contact-list svg {
    width: 20px;
    height: 20px;
    margin-right: 7px;
    flex: none;
  }
  .product-photo {
    position: absolute;
    left: 16px;
    top: 296px;
    width: 258px;
    height: 192px;
    border-radius: 4px;
    background: linear-gradient(180deg, var(--photo-dark) 0%, var(--photo-mid) 55%, var(--photo-light) 100%);
  }
  .card--back .brand {
    top: 0;
    height: 100%;
    gap: 14px;
    font-size: 48px;
    letter-spacing: 2px;
    color: var(--slate);
  }
  .card--back .brand__dot {
    width: 30px;
    height: 30px;
    border-radius: 50%;
    background: var(--slate-light);
  }
</style>
</head>
<body>
<main class="canvas">
  <section class="card card--front" aria-label="Card front">
    <div class="brand"><span class="brand__dot" aria-hidden="true"></span>SKYVANTEX</div>
    <div class="identity">
      <p class="identity__name">Marcus Pettibone</p>
      <p class="identity__tagline">Aerial Photo/Video and 3D Mapping/Modeling</p>
    </div>
    <ul class="contact-list">
      <li>
        <svg viewBox="0 0 24 24" aria-hidden="true"><path fill="var(--accent-red)" d="M8 2c-1.5 0-3 1.4-3 4 0 6 4 13 9 16 1.5.8 3 .3 3.6-.8l.8-1.5-3.5-2.5-1.3 1.2c-2-1.2-4-5-4.3-7.5l1.6-.8L10 5.5 8 2z"/></svg>
        571-806-3394
      </li>
      <li>
        <svg viewBox="0 0 24 24" aria-hidden="true"><rect x="2" y="5" width="20" height="14" fill="var(--accent-red)"/><path d="M2 5l10 8 10-8M2 19l7-7M22 19l-7-7" stroke="#fff" stroke-width="1.5" fill="none"/></svg>
        mqp@skyvantex.us
      </li>
      <li>
        <svg viewBox="0 0 24 24" aria-hidden="true"><circle cx="12" cy="12" r="10" fill="var(--accent-red)"/><path d="M2 12h20M12 2v20M4 7h16M4 17h16" stroke="#fff" stroke-width="1.3" fill="none"/><ellipse cx="12" cy="12" rx="4.5" ry="10" stroke="#fff" stroke-width="1.3" fill="none"/></svg>
        skyvantex.us
      </li>
    </ul>
    <div class="product-photo" role="img" aria-label="Photo of a quadcopter camera drone"></div>
  </section>

  <section class="card card--back" aria-label="Card back">
    <div class="brand"><span class="brand__dot" aria-hidden="true"></span>SKYVANTEX</div>
  </section>
</main>
</body>
</html>
```